Laundromat wall mural with logo, wash steps and soap dish instructions

Hi,
I am building a new laundromat and want to design a large wall mural containing a few different sections. The first piece would be a large image of my logo "Suds Harbor Laundromat" with my new tag line under it "A better Place to Wash". The next section would be general washing instructions: (step1) load clothes, (step 2) load soap, (step 3) select cycle (step 4) present payment (Quarters, Credit Card or Fennix/trove pay) (Step 5) Press start. Please use the wave from the logo to encase each of these 5 steps. Also please use an emblem in each wave to show each sections action. Such as they did in one of the example files I attached to this brief. The Final section would be the design for the soap compartment, describing where it goes. Please place the title "Where does the soap go?" above this section. The whole wall section will be 40 feet wide and 5 feet tall. I would like each section to flow aesthetically into the other. Feel free to use the logos waves and colors to bring everything together. I have attached examples of other store designs that I have found. The design will be above the washers that are placed against the wall.
I also placed a design of the mural that I wasn't completely impressed with so I opened the project to more designers.

Please let me know what other info you need.

Bests

Target Market(s)

laundromat customers

Industry/Entity Type

Laundromat

Font styles to use
Sans Serif

Colors
0054AA
0677BA
7BADD7
CADEEF
E8F1F8

Requirements
Must have
• The wave from my logo continuously flowing around the side and bottom borders.

```html
<!DOCTYPE html>
<html lang="en">
<head>
<meta charset="utf-8">
<title>Suds Harbor Laundromat – Wall Mural</title>
<link rel="stylesheet" href="https://fonts.googleapis.com/css2?family=Poppins:wght@500;600;700;800&display=swap">
<style>
  :root {
    --navy: #0054aa;
    --blue: #0677ba;
    --sky: #7badd7;
    --mist: #cadeef;
    --cloud: #e8f1f8;
    --title: #1f6fb5;
    --step-1: #6fc5e3;
    --step-2: #22a5d8;
    --step-3: #1a93c4;
    --step-4: #2a78bd;
    --step-5: #124e91;
    --wave-deep: #1592cc;
    --wave-mid: #2aa8dc;
    --wave-light: #7fcbe8;
    --cream: #fbfbf3;
    --white: #ffffff;
    --ink: #1b1b1b;
  }
  * { margin: 0; padding: 0; box-sizing: border-box; }
  html, body { width: 1200px; height: 450px; overflow: hidden; }
  body { font-family: "Poppins", sans-serif; }

  .mural {
    position: relative;
    width: 1200px;
    height: 450px;
    overflow: hidden;
    background: linear-gradient(180deg, #bde5f4 0%, #dff1f6 35%, var(--cream) 70%);
  }

  .border-waves { position: absolute; inset: 0; width: 1200px; height: 450px; }

  /* Brand block */
  .brand { position: absolute; left: 40px; top: 118px; width: 290px; }
  .brand-name {
    color: var(--title);
    font-weight: 800;
    font-size: 31px;
    line-height: 1.02;
    letter-spacing: 0.5px;
    text-transform: uppercase;
  }
  .tagline {
    position: absolute;
    left: 40px; top: 232px; width: 280px;
    text-align: center;
    color: var(--title);
    font-weight: 700;
    font-size: 34px;
    line-height: 1.02;
    letter-spacing: -1px;
  }

  /* Steps */
  .steps { position: absolute; left: 326px; top: 58px; display: flex; gap: 3px; }
  .step { position: relative; width: 108px; height: 282px; }
  .step-cap { position: absolute; left: 0; top: 0; width: 108px; height: 60px; }
  .step-body {
    position: absolute; left: 0; top: 38px; width: 108px; height: 244px;
    border-radius: 20px;
    display: flex; flex-direction: column; align-items: center;
    color: var(--white);
  }
  .step-label { margin-top: 6px; font-weight: 700; font-size: 17px; line-height: 1; }
  .step-number { font-weight: 800; font-size: 42px; line-height: 1; margin-top: 0; }
  .step-icon { width: 84px; height: 84px; margin-top: 8px; }
  .step-action {
    margin-top: auto; margin-bottom: 16px;
    font-weight: 700; font-size: 20px; line-height: 0.98;
    text-align: center; letter-spacing: -0.6px;
  }
  .step--1 .step-body { background: var(--step-1); }
  .step--2 .step-body { background: var(--step-2); }
  .step--3 .step-body { background: var(--step-3); }
  .step--4 .step-body { background: var(--step-4); }
  .step--5 .step-body { background: var(--step-5); }

  .pay-pill {
    display: flex; align-items: center; gap: 3px;
    margin-top: -6px;
    background: var(--white); border-radius: 8px;
    padding: 1px 5px;
    color: var(--ink); font-size: 6.5px; font-weight: 600;
  }
  .pay-pill svg { width: 9px; height: 9px; }

  /* Soap section */
  .soap-title {
    position: absolute; left: 925px; top: 82px; width: 210px;
    text-align: center;
    color: var(--title);
    font-weight: 700; font-size: 31px; line-height: 0.95; letter-spacing: -1px;
  }
  .dispenser-photo {
    position: absolute; left: 967px; top: 157px; width: 132px; height: 168px;
    border-radius: 6px 6px 10px 10px;
    background: linear-gradient(180deg, #6b6d72 0%, #8a8c90 55%, #a7a9ad 100%);
  }
  .soap-guide { position: absolute; left: 920px; top: 210px; width: 240px; height: 110px; }
  .soap-tag {
    position: absolute; color: var(--ink);
    font-size: 7px; font-weight: 500; line-height: 1.05; text-align: center;
  }
</style>
</head>
<body>
<main class="mural">

  <svg class="border-waves" viewBox="0 0 1200 450" aria-hidden="true">
    <!-- left side wave -->
    <path d="M0 150 C30 180 12 240 30 300 C45 350 80 370 120 380 L0 450 Z" fill="var(--wave-light)"/>
    <path d="M0 190 C25 240 10 290 40 340 C60 375 100 385 150 392 L0 450 Z" fill="var(--wave-mid)"/>
    <!-- right side wave -->
    <path d="M1200 260 C1175 300 1180 340 1150 370 C1120 395 1060 400 1000 395 L1200 450 Z" fill="var(--wave-light)"/>
    <path d="M1200 300 C1180 335 1170 365 1135 385 C1100 402 1050 405 990 402 L1200 450 Z" fill="var(--wave-mid)"/>
    <!-- bottom bands -->
    <path d="M0 385 C200 355 400 380 600 368 C800 356 1000 375 1200 372 L1200 450 L0 450 Z" fill="var(--wave-mid)"/>
    <path d="M0 405 C220 385 420 402 620 392 C820 382 1000 398 1200 392 L1200 450 L0 450 Z" fill="var(--wave-light)"/>
    <path d="M0 425 C250 410 450 420 650 412 C850 405 1020 418 1200 410 L1200 450 L0 450 Z" fill="var(--wave-deep)"/>
  </svg>

  <section class="brand">
    <h1 class="brand-name">Suds Harbor<br>Laundromat</h1>
  </section>
  <p class="tagline">A Better Place To Wash</p>

  <section class="steps">
    <article class="step step--1">
      <svg class="step-cap" viewBox="0 0 108 60" aria-hidden="true"><path d="M2 60 C2 30 25 8 54 8 C80 8 100 22 106 50 L106 60 Z" fill="var(--wave-mid)"/><path d="M30 20 C45 5 70 4 88 18" stroke="var(--white)" stroke-width="3" fill="none" opacity=".6"/></svg>
      <div class="step-body">
        <span class="step-label">STEP</span>
        <span class="step-number">01</span>
        <svg class="step-icon" viewBox="0 0 84 84" aria-hidden="true"><path d="M28 10 C34 16 50 16 56 10 L84 22 L84 40 L68 40 L68 82 L16 82 L16 40 L0 40 L0 22 Z" fill="var(--white)"/></svg>
        <span class="step-action">LOAD<br>CLOTHES</span>
      </div>
    </article>
    <article class="step step--2">
      <svg class="step-cap" viewBox="0 0 108 60" aria-hidden="true"><path d="M2 60 C2 30 25 8 54 8 C80 8 100 22 106 50 L106 60 Z" fill="var(--wave-mid)"/><path d="M30 20 C45 5 70 4 88 18" stroke="var(--white)" stroke-width="3" fill="none" opacity=".6"/></svg>
      <div class="step-body">
        <span class="step-label">STEP</span>
        <span class="step-number">02</span>
        <svg class="step-icon" viewBox="0 0 84 84" aria-hidden="true"><path d="M20 6 L46 6 L62 22 L66 16 L76 26 L70 32 L70 80 L10 80 C4 80 2 74 2 66 L2 40 C2 20 8 8 20 6 Z" fill="var(--white)"/><ellipse cx="24" cy="44" rx="9" ry="18" fill="var(--step-2)"/></svg>
        <span class="step-action">LOAD<br>SOAP</span>
      </div>
    </article>
    <article class="step step--3">
      <svg class="step-cap" viewBox="0 0 108 60" aria-hidden="true"><path d="M2 60 C2 30 25 8 54 8 C80 8 100 22 106 50 L106 60 Z" fill="var(--wave-mid)"/><path d="M30 20 C45 5 70 4 88 18" stroke="var(--white)" stroke-width="3" fill="none" opacity=".6"/></svg>
      <div class="step-body">
        <span class="step-label">STEP</span>
        <span class="step-number">03</span>
        <svg class="step-icon" viewBox="0 0 84 84" aria-hidden="true" fill="none" stroke="var(--white)" stroke-width="7" stroke-linecap="round"><path d="M24 20 C40 8 60 10 70 22"/><path d="M78 40 C80 58 68 72 52 76"/><path d="M30 74 C14 66 6 50 12 34"/><path d="M64 12 L72 22 L60 26" stroke-linejoin="round"/><path d="M46 68 L52 78 L42 82" stroke-linejoin="round"/><path d="M4 40 L12 32 L18 42" stroke-linejoin="round"/></svg>
        <span class="step-action">SELECT<br>CYCLE</span>
      </div>
    </article>
    <article class="step step--4">
      <svg class="step-cap" viewBox="0 0 108 60" aria-hidden="true"><path d="M2 60 C2 30 25 8 54 8 C80 8 100 22 106 50 L106 60 Z" fill="var(--wave-mid)"/><path d="M30 20 C45 5 70 4 88 18" stroke="var(--white)" stroke-width="3" fill="none" opacity=".6"/></svg>
      <div class="step-body">
        <span class="step-label">STEP</span>
        <span class="step-number">04</span>
        <svg class="step-icon" viewBox="0 0 84 84" aria-hidden="true"><rect x="26" y="4" width="30" height="32" rx="3" fill="none" stroke="var(--white)" stroke-width="5"/><rect x="36" y="4" width="6" height="28" fill="var(--white)"/><rect x="16" y="26" width="50" height="58" rx="6" fill="var(--white)"/><rect x="24" y="34" width="34" height="7" rx="2" fill="var(--step-4)"/><g fill="var(--step-4)"><circle cx="28" cy="50" r="3"/><circle cx="41" cy="50" r="3"/><circle cx="54" cy="50" r="3"/><circle cx="28" cy="61" r="3"/><circle cx="41" cy="61" r="3"/><circle cx="54" cy="61" r="3"/><circle cx="28" cy="72" r="3"/><circle cx="41" cy="72" r="3"/><circle cx="54" cy="72" r="3"/></g></svg>
        <div class="pay-pill">
          <svg viewBox="0 0 10 10" aria-hidden="true"><circle cx="5" cy="5" r="4.5" fill="var(--ink)"/></svg>
          <svg viewBox="0 0 10 10" aria-hidden="true"><rect x=".5" y="2" width="9" height="6" rx="1" fill="none" stroke="var(--ink)"/><rect x=".5" y="3.5" width="9" height="1.2" fill="var(--ink)"/></svg>
          <span>Fennix/trove pay</span>
        </div>
        <span class="step-action">PRESENT<br>PAYMENT</span>
      </div>
    </article>
    <article class="step step--5">
      <svg class="step-cap" viewBox="0 0 108 60" aria-hidden="true"><path d="M2 60 C2 30 25 8 54 8 C80 8 100 22 106 50 L106 60 Z" fill="var(--wave-mid)"/><path d="M30 20 C45 5 70 4 88 18" stroke="var(--white)" stroke-width="3" fill="none" opacity=".6"/></svg>
      <div class="step-body">
        <span class="step-label">STEP</span>
        <span class="step-number">05</span>
        <svg class="step-icon" viewBox="0 0 84 84" aria-hidden="true"><circle cx="34" cy="14" r="11" fill="none" stroke="var(--white)" stroke-width="5"/><path d="M30 14 C30 10 38 10 38 14 L38 44 L46 40 C50 38 56 40 58 44 L64 42 C68 42 72 46 72 52 L72 64 C72 76 62 84 50 84 L40 84 C30 84 20 78 10 62 C8 58 12 54 16 56 L30 64 Z" fill="var(--white)"/></svg>
        <span class="step-action">PRESS<br>START</span>
      </div>
    </article>
  </section>

  <h2 class="soap-title">Where does the soap go?</h2>
  <div class="dispenser-photo" role="img" aria-label="Photo of the washer soap dispenser tray with four compartments and lid open"></div>
  <svg class="soap-guide" viewBox="0 0 240 110" aria-hidden="true">
    <g fill="var(--title)" stroke="var(--white)" stroke-width="2">
      <circle cx="30" cy="38" r="15"/><circle cx="30" cy="76" r="15"/>
      <circle cx="191" cy="38" r="15"/><circle cx="191" cy="76" r="15"/>
    </g>
    <g fill="none" stroke="var(--white)" stroke-width="1.6">
      <circle cx="30" cy="38" r="6"/>
      <path d="M24 72 L36 72 L34 82 L26 82 Z M28 72 L28 78 M32 72 L32 78"/>
      <path d="M185 72 L197 72 L195 82 L187 82 Z M189 72 L189 78 M193 72 L193 78"/>
      <path d="M184 44 L194 32 M188 44 L198 44 L193 36 Z"/>
    </g>
    <g fill="none" stroke="var(--blue)" stroke-width="6" stroke-linecap="round">
      <path d="M48 34 C65 18 85 20 100 38"/>
      <path d="M48 72 C65 58 85 60 100 76"/>
      <path d="M173 34 C156 18 138 20 124 38"/>
      <path d="M173 72 C156 58 138 60 124 76"/>
    </g>
    <g fill="var(--blue)">
      <path d="M94 30 L106 44 L90 44 Z"/><path d="M94 68 L106 82 L90 82 Z"/>
      <path d="M130 30 L118 44 L134 44 Z"/><path d="M130 68 L118 82 L134 82 Z"/>
    </g>
  </svg>
  <span class="soap-tag" style="left:937px;top:215px;">Fabric<br>Softener</span>
  <span class="soap-tag" style="left:928px;top:305px;">Detergent</span>
  <span class="soap-tag" style="left:1085px;top:215px;">Liquid only<br>Detergent/Bleach</span>
  <span class="soap-tag" style="left:1097px;top:305px;">Detergent</span>

</main>
</body>
</html>
```